Truck Drivers Using App w/Jobsite Checklist

Looking for an 8" x 11" flyer that conveys to our customers (roofing contractors) that our drivers have tablets in each truck that have an app with a jobsite checklist that gives contractors less real time notifications and mistakes are caught with photos.
Should read something like this:
Ever wonder if your material has been delivered? We've got a solution for that!
All Trucks are equipped with dash-mounted tablet.
Here's what you get access to:
- Real Time Email Confirmation of Delivery
- Photos of Material Placement
- Before/After Photo of Driveway
- Material List of Products Delivered
- Homeowner Sign Off
Maybe a collage of the different photos available.
Target Market(s)
Roofing/Building Contractors
Industry/Entity Type
Roofing
Requirements
Must have
- website: www.harborfinchdepot.com
- tagline: Building Relationships, Building Trust - a Tradition Since 1905
- Photoshop format for further editing
Nice to have
- A smooth look to it.
- A collage of the photos avail on app

```html
<!DOCTYPE html>
<html lang="en">
<head>
<meta charset="utf-8">
<title>Harbor Finch Depot – Delivery Flyer</title>
<link rel="stylesheet" href="https://fonts.googleapis.com/css2?family=Jost:wght@300;400;700;800&family=Roboto+Condensed:wght@400;700&display=swap">
<style>
  :root{
    --sky-light:#cfe4f7;
    --sky:#a8cbeb;
    --royal:#1d5fae;
    --navy:#173f7a;
    --ink:#1d2b45;
    --white:#ffffff;
    --photo-a:#8fa9bf;
    --photo-b:#c9d3da;
  }
  html,body{margin:0;padding:0;width:850px;height:1200px;overflow:hidden;background:#e9e9e9;}
  .flyer{
    position:relative;width:850px;height:1200px;overflow:hidden;
    background:linear-gradient(160deg,var(--sky-light) 0%,var(--sky) 100%);
    font-family:"Jost",sans-serif;color:var(--ink);
  }
  .collage{position:absolute;left:0;top:0;width:850px;height:1200px;}
  .brand{
    position:absolute;left:41px;top:70px;width:246px;height:110px;
    display:flex;align-items:center;gap:14px;
  }
  .brand-dot{width:34px;height:34px;border-radius:50%;background:var(--navy);flex:none;}
  .brand-name{font-family:"Jost",sans-serif;font-weight:700;font-size:34px;line-height:1.05;color:var(--navy);}
  .headline{
    position:absolute;left:50px;top:318px;margin:0;
    font-weight:800;font-size:50px;line-height:52px;color:var(--royal);text-transform:uppercase;
  }
  .tagline{position:absolute;left:52px;top:478px;margin:0;font-weight:400;font-size:32px;color:var(--ink);}
  .access-banner{
    position:absolute;left:0;top:565px;width:455px;height:44px;background:var(--navy);
    clip-path:polygon(0 0,92% 0,100% 50%,92% 100%,0 100%);
    color:var(--white);font-family:"Roboto Condensed",sans-serif;font-weight:700;font-size:26px;
    line-height:44px;padding-left:54px;box-sizing:border-box;
  }
  .benefits{
    position:absolute;left:50px;top:625px;margin:0;padding:0;list-style:none;
    font-family:"Roboto Condensed",sans-serif;font-size:28px;line-height:42px;color:var(--ink);
  }
  .benefits li{display:flex;align-items:center;gap:12px;}
  .benefits li::before{
    content:"";width:0;height:0;border-left:11px solid var(--royal);
    border-top:7px solid transparent;border-bottom:7px solid transparent;
  }
  .driver-photo{
    position:absolute;left:0;top:850px;width:276px;height:350px;
    background:linear-gradient(170deg,#b7c8d6 0%,#d6d9a0 60%,#8a97a8 100%);
  }
  .speech-bubble{
    position:absolute;left:262px;top:894px;width:255px;height:118px;box-sizing:border-box;
    background:var(--navy);border-radius:14px;color:var(--white);
    font-family:"Roboto Condensed",sans-serif;font-size:21px;line-height:26px;padding:18px 16px;
  }
  .speech-bubble::before{
    content:"";position:absolute;left:-22px;top:40px;border-right:24px solid var(--navy);
    border-top:12px solid transparent;border-bottom:12px solid transparent;
  }
  .call-label{position:absolute;left:253px;top:1040px;font-size:32px;font-weight:400;}
  .call-number{
    position:absolute;left:253px;top:1080px;font-size:36px;font-weight:700;
    display:flex;align-items:center;gap:8px;
  }
  .footer-bar{
    position:absolute;left:207px;top:1137px;width:400px;height:63px;background:var(--royal);
    display:flex;align-items:center;gap:10px;padding-left:160px;box-sizing:border-box;
    color:var(--white);font-size:20px;font-weight:700;
  }
  .globe{width:18px;height:18px;border:2px solid var(--white);border-radius:50%;flex:none;box-sizing:border-box;}
</style>
</head>
<body>
<main class="flyer">
  <svg class="collage" viewBox="0 0 370 510" preserveAspectRatio="none" aria-hidden="false">
    <defs>
      <linearGradient id="photoTone" x1="0" y1="0" x2="1" y2="1">
        <stop offset="0" stop-color="#9fb6c9"/><stop offset="1" stop-color="#d4d8dc"/>
      </linearGradient>
      <linearGradient id="bundleTone" x1="0" y1="0" x2="1" y2="1">
        <stop offset="0" stop-color="#7fa6cf"/><stop offset="1" stop-color="#e4e0e2"/>
      </linearGradient>
      <linearGradient id="treeTone" x1="0" y1="0" x2="0" y2="1">
        <stop offset="0" stop-color="#6f8a6a"/><stop offset="1" stop-color="#c9c2b3"/>
      </linearGradient>
    </defs>
    <polygon points="300,0 370,0 370,70" fill="#b9d6f0"/>
    <polygon role="img" aria-label="Dash-mounted tablet photo" points="255,0 370,0 370,95 310,40" fill="url(#photoTone)" stroke="#fff" stroke-width="5" vector-effect="non-scaling-stroke"/>
    <polygon role="img" aria-label="Shingle bundles delivered on roof photo" points="170,95 260,40 360,100 270,170" fill="url(#bundleTone)" stroke="#fff" stroke-width="6" vector-effect="non-scaling-stroke"/>
    <polygon points="340,140 370,110 370,200" fill="#1d5fae"/>
    <polygon role="img" aria-label="Delivery truck photo" points="275,230 320,185 370,215 370,300 350,300" fill="url(#photoTone)" stroke="#fff" stroke-width="5" vector-effect="non-scaling-stroke"/>
    <polygon role="img" aria-label="Material placed in driveway photo" points="200,310 280,230 365,335 270,400" fill="url(#treeTone)" stroke="#fff" stroke-width="6" vector-effect="non-scaling-stroke"/>
    <polygon points="335,360 370,330 370,395" fill="#1d5fae"/>
    <polygon role="img" aria-label="Driveway after delivery photo" points="250,510 260,440 330,400 370,440 370,510" fill="url(#photoTone)" stroke="#fff" stroke-width="5" vector-effect="non-scaling-stroke"/>
  </svg>

  <div class="brand">
    <span class="brand-dot"></span>
    <span class="brand-name">Harbor Finch<br>Depot</span>
  </div>

  <h1 class="headline">Building<br>Relationships<br>Building Trust</h1>
  <p class="tagline">A TRADITION SINCE 1905</p>

  <div class="access-banner">Here's what you get access to:</div>
  <ul class="benefits">
    <li>Real Time Email Confirmation of Delivery</li>
    <li>Photos of Material Placement</li>
    <li>Before/After Photo of Driveway</li>
    <li>Material List of Products Delivered</li>
    <li>Homeowner Sign Off</li>
  </ul>

  <div class="driver-photo" role="img" aria-label="Smiling driver in safety vest holding a tablet"></div>

  <div class="speech-bubble">Ever wonder if your material has been delivered? We've got a solution for that!</div>

  <div class="call-label">Call now:</div>
  <div class="call-number">
    <svg width="30" height="30" viewBox="0 0 24 24" aria-hidden="true"><path d="M6.6 10.8a15 15 0 0 0 6.6 6.6l2.2-2.2c.3-.3.7-.4 1-.2 1.1.4 2.3.6 3.6.6.6 0 1 .4 1 1V20c0 .6-.4 1-1 1A17 17 0 0 1 3 4c0-.6.4-1 1-1h3.5c.6 0 1 .4 1 1 0 1.3.2 2.5.6 3.6.1.3 0 .7-.2 1z" fill="#1d2b45"/></svg>
    +1555 010 204
  </div>

  <div class="footer-bar"><span class="globe"></span>www.harborfinchdepot.com</div>
</main>
</body>
</html>
```